Flavour Wheel - Illustrator Graph

I need my basic layout, from the sample I provided, turned into a professional looking flavour wheel.

I have attached a sample of a final design I like, but please use your own creativity also.

All the exact words I need are on the uploaded illustration.

I would need the file supplied to me in .ai

Industry/Entity Type

Wheel

Font styles to use
Sans Serif

Colors

Designer to choose colors to be used in the design.

Requirements
Must have
• Files must be supplied in .ai format with fonts not outlined.
• I need each segment separated so I can change the colours if needed myself.
Nice to have
• I like small white gaps between the sections.

```html
<!DOCTYPE html>
<html lang="en">
<head>
<meta charset="utf-8">
<title>Flavour Wheel</title>
<link rel="stylesheet" href="https://fonts.googleapis.com/css2?family=Roboto+Condensed:wght@700&family=Roboto:wght@700&display=swap">
<style>
  :root{
    --paper:#ffffff;
    --label:#ffffff;
    /* sour */
    --sour:#f5cc00; --bitter:#d6a000; --citric:#f5c500; --tamarind:#d69a00;
    --vinegary:#b5890a; --vinegar-list:#a67c00; --citrus:#8c6e1a; --citrus-list:#6b5420;
    /* earthy */
    --earthy:#93d600; --floral:#7cbf00; --floral-list:#3dae2b; --herby:#6e9a0a;
    --nutty:#4f5a10; --buttery:#4a4a0a; --herb-list:#4a8c2a; --butter-list:#2e5e1e;
    /* sweet */
    --sweet:#e57acb; --fruity:#d23db7; --sugary:#c4179f; --caramel:#a3148a;
    --fruit-list:#a8386f; --sugar-list:#8e1c5c; --caramel-list:#6a2350;
    /* salty */
    --salty:#1ccfc4; --charred:#10b5aa; --briney:#0e9a8e; --charred-list:#1e9a88; --briney-list:#0c4e55;
    /* savoury */
    --savoury:#f7902a; --meatiness:#e87410; --umami:#d66106; --savoury-list:#ff5a00;
    /* spicy */
    --spicy:#e8503f; --chilli:#c8342a; --peppery:#a8262a; --cajun:#7a2a22;
    --chilli-list:#db4310; --pepper-list:#d0323a;
    /* smokey */
    --smokey:#c8c8c8; --woody:#9a9a9a; --smoke-fruity:#8a8a8a; --acrid:#6c6c6c;
    --wood-list:#8e9a94; --creosote-list:#4a5553;
  }
  html,body{margin:0;padding:0;width:1200px;height:971px;overflow:hidden;background:var(--paper);}
  .wheel{display:block;width:1200px;height:971px;}
  .segment{stroke:var(--paper);stroke-width:3;stroke-linejoin:round;}
  .label{fill:var(--label);text-anchor:middle;dominant-baseline:central;}
  .label--category{font-family:"Roboto",Arial,sans-serif;font-weight:700;font-size:12.5px;}
  .label--group{font-family:"Roboto",Arial,sans-serif;font-weight:700;font-size:11px;}
  .label--item{font-family:"Roboto Condensed","Arial Narrow",sans-serif;font-weight:700;font-size:8.6px;}
</style>
</head>
<body>
<svg class="wheel" viewBox="-445 -355 877 710" xmlns="http://www.w3.org/2000/svg" role="img" aria-label="Flavour wheel">

  <!-- categories -->
  <g class="ring ring--categories">
    <path class="segment" style="fill:var(--sour)" d="M-56.64,-136.73 A148,148 0 0 1 56.64,-136.73 L19.90,-48.04 A52,52 0 0 0 -19.90,-48.04 Z"/>
    <path class="segment" style="fill:var(--earthy)" d="M56.64,-136.73 A148,148 0 0 1 148,0 L52,0 A52,52 0 0 0 19.90,-48.04 Z"/>
    <path class="segment" style="fill:var(--sweet)" d="M148,0 A148,148 0 0 1 86.99,119.73 L30.57,42.07 A52,52 0 0 0 52,0 Z"/>
    <path class="segment" style="fill:var(--salty)" d="M86.99,119.73 A148,148 0 0 1 0,148 L0,52 A52,52 0 0 0 30.57,42.07 Z"/>
    <path class="segment" style="fill:var(--savoury)" d="M0,148 A148,148 0 0 1 -104.65,104.65 L-36.77,36.77 A52,52 0 0 0 0,52 Z"/>
    <path class="segment" style="fill:var(--spicy)" d="M-104.65,104.65 A148,148 0 0 1 -148,0 L-52,0 A52,52 0 0 0 -36.77,36.77 Z"/>
    <path class="segment" style="fill:var(--smokey)" d="M-148,0 A148,148 0 0 1 -56.64,-136.73 L-19.90,-48.04 A52,52 0 0 0 -52,0 Z"/>
  </g>

  <!-- groups -->
  <g class="ring ring--groups">
    <path class="segment" style="fill:var(--bitter)" d="M-81.13,-195.86 A212,212 0 0 1 -27.67,-210.19 L-19.32,-146.73 A148,148 0 0 0 -56.64,-136.73 Z"/>
    <path class="segment" style="fill:var(--vinegary)" d="M-27.67,-210.19 A212,212 0 0 1 27.67,-210.19 L19.32,-146.73 A148,148 0 0 0 -19.32,-146.73 Z"/>
    <path class="segment" style="fill:var(--citrus)" d="M27.67,-210.19 A212,212 0 0 1 81.13,-195.86 L56.64,-136.73 A148,148 0 0 0 19.32,-146.73 Z"/>
    <path class="segment" style="fill:var(--floral)" d="M81.13,-195.86 A212,212 0 0 1 134.49,-163.88 L93.89,-114.41 A148,148 0 0 0 56.64,-136.73 Z"/>
    <path class="segment" style="fill:var(--herby)" d="M134.49,-163.88 A212,212 0 0 1 176.27,-117.78 L123.06,-82.22 A148,148 0 0 0 93.89,-114.41 Z"/>
    <path class="segment" style="fill:var(--nutty)" d="M176.27,-117.78 A212,212 0 0 1 202.87,-61.54 L141.63,-42.96 A148,148 0 0 0 123.06,-82.22 Z"/>
    <path class="segment" style="fill:var(--buttery)" d="M202.87,-61.54 A212,212 0 0 1 212,0 L148,0 A148,148 0 0 0 141.63,-42.96 Z"/>
    <path class="segment" style="fill:var(--fruity)" d="M212,0 A212,212 0 0 1 201.62,65.51 L140.76,45.73 A148,148 0 0 0 148,0 Z"/>
    <path class="segment" style="fill:var(--sugary)" d="M201.62,65.51 A212,212 0 0 1 171.51,124.61 L119.73,86.99 A148,148 0 0 0 140.76,45.73 Z"/>
    <path class="segment" style="fill:var(--caramel)" d="M171.51,124.61 A212,212 0 0 1 124.61,171.51 L86.99,119.73 A148,148 0 0 0 119.73,86.99 Z"/>
    <path class="segment" style="fill:var(--charred)" d="M124.61,171.51 A212,212 0 0 1 65.51,201.62 L45.73,140.76 A148,148 0 0 0 86.99,119.73 Z"/>
    <path class="segment" style="fill:var(--briney)" d="M65.51,201.62 A212,212 0 0 1 0,212 L0,148 A148,148 0 0 0 45.73,140.76 Z"/>
    <path class="segment" style="fill:var(--meatiness)" d="M0,212 A212,212 0 0 1 -81.13,195.86 L-56.64,136.73 A148,148 0 0 0 0,148 Z"/>
    <path class="segment" style="fill:var(--umami)" d="M-81.13,195.86 A212,212 0 0 1 -149.91,149.91 L-104.65,104.65 A148,148 0 0 0 -56.64,136.73 Z"/>
    <path class="segment" style="fill:var(--chilli)" d="M-149.91,149.91 A212,212 0 0 1 -183.60,106 L-128.17,74 A148,148 0 0 0 -104.65,104.65 Z"/>
    <path class="segment" style="fill:var(--peppery)" d="M-183.60,106 A212,212 0 0 1 -204.78,54.87 L-142.96,38.31 A148,148 0 0 0 -128.17,74 Z"/>
    <path class="segment" style="fill:var(--cajun)" d="M-204.78,54.87 A212,212 0 0 1 -212,0 L-148,0 A148,148 0 0 0 -142.96,38.31 Z"/>
    <path class="segment" style="fill:var(--woody)" d="M-212,0 A212,212 0 0 1 -195.86,-81.13 L-136.73,-56.64 A148,148 0 0 0 -148,0 Z"/>
    <path class="segment" style="fill:var(--smoke-fruity)" d="M-195.86,-81.13 A212,212 0 0 1 -149.91,-149.91 L-104.65,-104.65 A148,148 0 0 0 -136.73,-56.64 Z"/>
    <path class="segment" style="fill:var(--acrid)" d="M-149.91,-149.91 A212,212 0 0 1 -81.13,-195.86 L-56.64,-136.73 A148,148 0 0 0 -104.65,-104.65 Z"/>
  </g>

  <!-- item lists -->
  <g class="ring ring--items">
    <path class="segment" style="fill:var(--citric)" d="M-114.80,-277.16 A300,300 0 0 1 -64.93,-292.89 L-45.89,-206.98 A212,212 0 0 0 -81.13,-195.86 Z"/>
    <path class="segment" style="fill:var(--tamarind)" d="M-64.93,-292.89 A300,300 0 0 1 -39.16,-297.43 L-27.67,-210.19 A212,212 0 0 0 -45.89,-206.98 Z"/>
    <path class="segment" style="fill:var(--vinegar-list)" d="M-39.16,-297.43 A300,300 0 0 1 39.16,-297.43 L27.67,-210.19 A212,212 0 0 0 -27.67,-210.19 Z"/>
    <path class="segment" style="fill:var(--citrus-list)" d="M39.16,-297.43 A300,300 0 0 1 114.80,-277.16 L81.13,-195.86 A212,212 0 0 0 27.67,-210.19 Z"/>
    <path class="segment" style="fill:var(--floral-list)" d="M114.80,-277.16 A300,300 0 0 1 190.32,-231.90 L134.49,-163.88 A212,212 0 0 0 81.13,-195.86 Z"/>
    <path class="segment" style="fill:var(--herb-list)" d="M190.32,-231.90 A300,300 0 0 1 287.08,-87.08 L202.87,-61.54 A212,212 0 0 0 134.49,-163.88 Z"/>
    <path class="segment" style="fill:var(--butter-list)" d="M287.08,-87.08 A300,300 0 0 1 300,0 L212,0 A212,212 0 0 0 202.87,-61.54 Z"/>
    <path class="segment" style="fill:var(--fruit-list)" d="M300,0 A300,300 0 0 1 285.32,92.71 L201.62,65.51 A212,212 0 0 0 212,0 Z"/>
    <path class="segment" style="fill:var(--sugar-list)" d="M285.32,92.71 A300,300 0 0 1 242.71,176.34 L171.51,124.61 A212,212 0 0 0 201.62,65.51 Z"/>
    <path class="segment" style="fill:var(--caramel-list)" d="M242.71,176.34 A300,300 0 0 1 176.34,242.71 L124.61,171.51 A212,212 0 0 0 171.51,124.61 Z"/>
    <path class="segment" style="fill:var(--charred-list)" d="M176.34,242.71 A300,300 0 0 1 92.71,285.32 L65.51,201.62 A212,212 0 0 0 124.61,171.51 Z"/>
    <path class="segment" style="fill:var(--briney-list)" d="M92.71,285.32 A300,300 0 0 1 0,300 L0,212 A212,212 0 0 0 65.51,201.62 Z"/>
    <path class="segment" style="fill:var(--savoury-list)" d="M0,300 A300,300 0 0 1 -212.13,212.13 L-149.91,149.91 A212,212 0 0 0 0,212 Z"/>
    <path class="segment" style="fill:var(--chilli-list)" d="M-212.13,212.13 A300,300 0 0 1 -259.81,150 L-183.60,106 A212,212 0 0 0 -149.91,149.91 Z"/>
    <path class="segment" style="fill:var(--pepper-list)" d="M-259.81,150 A300,300 0 0 1 -300,0 L-212,0 A212,212 0 0 0 -183.60,106 Z"/>
    <path class="segment" style="fill:var(--wood-list)" d="M-300,0 A300,300 0 0 1 -212.13,-212.13 L-149.91,-149.91 A212,212 0 0 0 -212,0 Z"/>
    <path class="segment" style="fill:var(--creosote-list)" d="M-212.13,-212.13 A300,300 0 0 1 -114.80,-277.16 L-81.13,-195.86 A212,212 0 0 0 -149.91,-149.91 Z"/>
  </g>

  <!-- category labels -->
  <g class="labels labels--categories">
    <text class="label label--category" x="0" y="-100">Sour</text>
    <text class="label label--category" x="83.15" y="-55.56" transform="rotate(56.25 83.15 -55.56)">Earthy</text>
    <text class="label label--category" x="89.10" y="45.40" transform="rotate(-63 89.10 45.40)">Sweet</text>
    <text class="label label--category" x="30.90" y="95.11" transform="rotate(-18 30.90 95.11)">Salty</text>
    <text class="label label--category" x="-38.27" y="92.39" transform="rotate(22.5 -38.27 92.39)">Savoury</text>
    <text class="label label--category" x="-92.39" y="38.27" transform="rotate(67.5 -92.39 38.27)">Spicy</text>
    <text class="label label--category" x="-83.15" y="-55.56" transform="rotate(-56.25 -83.15 -55.56)">Smokey</text>
  </g>

  <!-- group labels -->
  <g class="labels labels--groups">
    <text class="label label--group" x="-46.59" y="-173.87" transform="rotate(-105 -46.59 -173.87)">Bitter</text>
    <text class="label label--group" x="0" y="-180" transform="rotate(-90 0 -180)">Vinegary</text>
    <text class="label label--group" x="46.59" y="-173.87" transform="rotate(-75 46.59 -173.87)">Citrus</text>
    <text class="label label--group" x="92.54" y="-154.39" transform="rotate(-59.06 92.54 -154.39)">Floral</text>
    <text class="label label--group" x="133.37" y="-120.88" transform="rotate(-42.19 133.37 -120.88)">Herby</text>
    <text class="label label--group" x="162.72" y="-76.96" transform="rotate(-25.31 162.72 -76.96)">Nutty</text>
    <text class="label label--group" x="178.05" y="-26.41" transform="rotate(-8.44 178.05 -26.41)">Buttery</text>
    <text class="label label--group" x="177.78" y="28.16" transform="rotate(9 177.78 28.16)">Fruity</text>
    <text class="label label--group" x="160.38" y="81.72" transform="rotate(27 160.38 81.72)">Sugary</text>
    <text class="label label--group" x="127.28" y="127.28" transform="rotate(45 127.28 127.28)">Caramel</text>
    <text class="label label--group" x="81.72" y="160.38" transform="rotate(63 81.72 160.38)">Charred</text>
    <text class="label label--group" x="28.16" y="177.78" transform="rotate(81 28.16 177.78)">Briney</text>
    <text class="label label--group" x="-35.12" y="176.54" transform="rotate(-78.75 -35.12 176.54)">Meatiness</text>
    <text class="label label--group" x="-100" y="149.66" transform="rotate(-56.25 -100 149.66)">Umami</text>
    <text class="label label--group" x="-142.80" y="109.58" transform="rotate(-37.5 -142.80 109.58)">Chilli</text>
    <text class="label label--group" x="-166.30" y="68.88" transform="rotate(-22.5 -166.30 68.88)">Peppery</text>
    <text class="label label--group" x="-178.46" y="23.50" transform="rotate(-7.5 -178.46 23.50)">Cajun</text>
    <text class="label label--group" x="-176.54" y="-35.12" transform="rotate(11.25 -176.54 -35.12)">Woody</text>
    <text class="label label--group" x="-149.66" y="-100" transform="rotate(33.75 -149.66 -100)">Fruity</text>
    <text class="label label--group" x="-100" y="-149.66" transform="rotate(56.25 -100 -149.66)">Acrid</text>
  </g>

  <!-- item labels -->
  <g class="labels labels--items">
    <text class="label label--item" transform="translate(-76.98 -244.15) rotate(-107.5)"><tspan x="0" dy="-5">Citric Acid</tspan><tspan x="0" dy="10">Cocktail Bitter</tspan></text>
    <text class="label label--item" transform="translate(-44.45 -252.11) rotate(-100)"><tspan x="0">Tamarind</tspan></text>
    <text class="label label--item" transform="translate(0 -256) rotate(-90)"><tspan x="0" dy="-10">Rice Vinegar</tspan><tspan x="0" dy="10">Balsamic Vinegar</tspan><tspan x="0" dy="10">Apple Cider Vinegar</tspan></text>
    <text class="label label--item" transform="translate(66.26 -247.28) rotate(-75)"><tspan x="0" dy="-15">Sumac</tspan><tspan x="0" dy="10">Zests</tspan><tspan x="0" dy="10">Lime</tspan><tspan x="0" dy="10">Lemmon</tspan></text>
    <text class="label label--item" transform="translate(131.61 -219.58) rotate(-59.06)"><tspan x="0" dy="-10">Coriander</tspan><tspan x="0" dy="10">Celery</tspan><tspan x="0" dy="10">Tea</tspan></text>
    <text class="label label--item" transform="translate(212.86 -142.23) rotate(-33.75)"><tspan x="0" dy="-67.6">Sage</tspan><tspan x="0" dy="10.4">Oregano</tspan><tspan x="0" dy="10.4">Thyme</tspan><tspan x="0" dy="10.4">Rosemary</tspan><tspan x="0" dy="10.4">Bay Leaf</tspan><tspan x="0" dy="10.4">Fennel</tspan><tspan x="0" dy="10.4">Five Spice</tspan><tspan x="0" dy="10.4">Nutmeg</tspan><tspan x="0" dy="10.4">Turmeric</tspan><tspan x="0" dy="10.4">Star Anise</tspan><tspan x="0" dy="10.4">Cinnamon</tspan><tspan x="0" dy="10.4">Clove</tspan><tspan x="0" dy="10.4">Pecan</tspan><tspan x="0" dy="10.4">Coffee</tspan></text>
    <text class="label label--item" transform="translate(253.23 -37.56) rotate(-8.44)"><tspan x="0">Butter</tspan></text>
    <text class="label label--item" transform="translate(252.85 40.05) rotate(9)"><tspan x="0" dy="-11">Fruit Juice</tspan><tspan x="0" dy="11">Fruits</tspan><tspan x="0" dy="11">Sauce/Ketchp</tspan></text>
    <text class="label label--item" transform="translate(228.10 116.22) rotate(27)"><tspan x="0" dy="-11">Cola</tspan><tspan x="0" dy="11">Agave Nectar</tspan><tspan x="0" dy="11">Sugars</tspan></text>
    <text class="label label--item" transform="translate(181.02 181.02) rotate(45)"><tspan x="0" dy="-11">Honey</tspan><tspan x="0" dy="11">Molasses</tspan><tspan x="0" dy="11">Maple Syrup</tspan></text>
    <text class="label label--item" transform="translate(116.22 228.10) rotate(63)"><tspan x="0" dy="-15">Anchovies</tspan><tspan x="0" dy="10">Garlic</tspan><tspan x="0" dy="10">Sea Salt</tspan><tspan x="0" dy="10">Kosher Salt</tspan></text>
    <text class="label label--item" transform="translate(40.05 252.85) rotate(81)"><tspan x="0" dy="-15">Soy Sauce</tspan><tspan x="0" dy="10">Fish Sauce</tspan><tspan x="0" dy="10">Worcestershire</tspan><tspan x="0" dy="10">Seasoning Sauce</tspan></text>
    <text class="label label--item" transform="translate(-97.97 236.51) rotate(-67.5)"><tspan x="0" dy="-22">MSG</tspan><tspan x="0" dy="11">Yeastmite</tspan><tspan x="0" dy="11">Lard</tspan><tspan x="0" dy="11">Stocks</tspan><tspan x="0" dy="11">Phosphates</tspan></text>
    <text class="label label--item" transform="translate(-203.10 155.84) rotate(-37.5)"><tspan x="0" dy="-27.6">Onion</tspan><tspan x="0" dy="9.2">Schechuan</tspan><tspan x="0" dy="9.2">Allspice</tspan><tspan x="0" dy="9.2">Cumin</tspan><tspan x="0" dy="9.2">Pepper</tspan><tspan x="0" dy="9.2">Wasabi</tspan><tspan x="0" dy="9.2">Wasabi</tspan></text>
    <text class="label label--item" transform="translate(-247.28 66.26) rotate(-15)"><tspan x="0" dy="-33">Paprika</tspan><tspan x="0" dy="11">Mustard</tspan><tspan x="0" dy="11">Red Pepper</tspan><tspan x="0" dy="11">Habanero</tspan><tspan x="0" dy="11">Hot Sauce</tspan><tspan x="0" dy="11">Jalapeno</tspan><tspan x="0" dy="11">Chipotle</tspan></text>
    <text class="label label--item" transform="translate(-236.51 -97.97) rotate(22.5)"><tspan x="0" dy="-22">Bourbon</tspan><tspan x="0" dy="11">Whisky</tspan><tspan x="0" dy="11">Charcoal</tspan><tspan x="0" dy="11">Fruit Woods</tspan><tspan x="0" dy="11">Hard Woods</tspan></text>
    <text class="label label--item" transform="translate(-142.23 -212.86) rotate(56.25)"><tspan x="0">Creosote</tspan></text>
  </g>
</svg>
</body>
</html>
```